Ridgecrest Ag, LLC
Business cards, letterhead, envelopes
Project: Ridgecrest Ag, LLC
Ridgecrest Ag, LLC - Consulting
Creative Brief
Professional
Warren Colbeck
P.O. Box 517 Monterey, CA 93940
warren@ridgecrestag-example.com
1. I want to use my logo and will upload it. 2. I like clean, uncluttered design. 3. OK to think a little out of the box. 4. May be OK to use a different font than logo. 5. May be OK to use tagline "same dirt - new rules" differently (i.e., not right under Ridgecrest Ag as shown in logo).

```html
<!DOCTYPE html>
<html lang="en">
<head>
<meta charset="utf-8">
<title>Ridgecrest Ag, LLC · Business Cards</title>
<link href="https://fonts.googleapis.com/css2?family=Source+Sans+3:wght@400;600&display=swap" rel="stylesheet">
<style>
  :root {
    --maroon: #560b0d;
    --gold: #fdbd5b;
    --white: #ffffff;
    --page: #ffffff;
    --edge: #b9b9b9;
  }
  * { box-sizing: border-box; margin: 0; padding: 0; }
  html, body { width: 1200px; height: 744px; overflow: hidden; background: var(--page); }
  body { position: relative; font-family: "Source Sans 3", Arial, sans-serif; }

  .card {
    position: absolute;
    width: 562px;
    height: 296px;
    border: 1px solid var(--edge);
    overflow: hidden;
  }
  .card--front { left: 34px; top: 32px; background: var(--white); }
  .card--back-white { left: 614px; top: 32px; background: var(--white); }
  .card--back-maroon { left: 34px; top: 352px; background: var(--maroon); }
  .card--back-gold { left: 614px; top: 352px; background: var(--gold); }

  .swoosh { position: absolute; inset: 0; width: 100%; height: 100%; }

  .wordmark {
    display: flex;
    align-items: center;
    gap: 12px;
    font-weight: 600;
    text-transform: uppercase;
    letter-spacing: 0.08em;
    white-space: nowrap;
  }
  .wordmark__dot { border-radius: 50%; flex: none; }

  .card--front .wordmark {
    position: absolute; left: 20px; top: 56px;
    font-size: 25px; color: var(--maroon);
  }
  .card--front .wordmark__dot { width: 12px; height: 12px; background: var(--gold); }

  .card--centered .wordmark {
    position: absolute; left: 0; right: 0; top: 0; bottom: 0;
    justify-content: center; font-size: 40px;
  }
  .card--centered .wordmark__dot { width: 18px; height: 18px; }
  .card--back-white .wordmark { color: var(--maroon); }
  .card--back-white .wordmark__dot { background: var(--gold); }
  .card--back-maroon .wordmark { color: var(--white); }
  .card--back-maroon .wordmark__dot { background: var(--gold); }
  .card--back-gold .wordmark { color: var(--maroon); }
  .card--back-gold .wordmark__dot { background: var(--maroon); }

  .holder-name {
    position: absolute; right: 18px; top: 116px;
    font-size: 22px; font-weight: 400; color: var(--maroon);
  }
  .contact {
    position: absolute; right: 18px; top: 226px;
    font-style: normal; text-align: right;
    font-size: 12.5px; line-height: 18px; color: var(--white);
  }
</style>
</head>
<body>

  <section class="card card--front" aria-label="Business card front">
    <svg class="swoosh" viewBox="0 0 562 296" preserveAspectRatio="none" aria-hidden="true">
      <path d="M0 198 C 160 160, 360 130, 562 128 L562 296 L0 296 Z" fill="var(--gold)"/>
      <path d="M0 222 C 170 186, 370 164, 562 164 L562 296 L0 296 Z" fill="var(--maroon)"/>
    </svg>
    <div class="wordmark"><span class="wordmark__dot"></span>Ridgecrest Ag</div>
    <p class="holder-name">Warren Colbeck</p>
    <address class="contact">
      P.O. Box 517, Monterey, CA 93940<br>
      Cell: (831) 555-0148 | Fax: (831) 555-0172<br>
      Email: warren@ridgecrestag-example.com
    </address>
  </section>

  <section class="card card--back-white card--centered" aria-label="Card back, white">
    <div class="wordmark"><span class="wordmark__dot"></span>Ridgecrest Ag</div>
  </section>

  <section class="card card--back-maroon card--centered" aria-label="Card back, maroon">
    <div class="wordmark"><span class="wordmark__dot"></span>Ridgecrest Ag</div>
  </section>

  <section class="card card--back-gold card--centered" aria-label="Card back, gold">
    <div class="wordmark"><span class="wordmark__dot"></span>Ridgecrest Ag</div>
  </section>

</body>
</html>
```